TRV Flyer

We need a professional design for flyers that we produce. The attached event draft is typical of the majority of flyers we will produce, and is the one that we need to do right now.

We would also like the source files for the design. We don’t have Corel Draw, but can work with any files produced in Adobe Creative Suite products.

Target Market(s)

Owners of residential apartments

Industry/Entity Type

Non-Profit

Requirements
Must have
• Design must be complimentary to our new website design at www.trv.org.au so we can establish consistent branding.
• Any fonts used must be freely avalaible standard fonts used in Microsoft Word

```html
<!DOCTYPE html>
<html lang="en">
<head>
<meta charset="utf-8">
<title>TRV Educational Workshop</title>
<link href="https://fonts.googleapis.com/css2?family=Arimo:ital,wght@0,400;0,700;1,700&family=Roboto+Condensed:wght@700&display=swap" rel="stylesheet">
<style>
  :root {
    --navy: #2f4d82;
    --ink-navy: #2b3f7a;
    --gold: #bf9237;
    --text: #1d1d1f;
    --rule: #4a4a4a;
    --box-grey: #e3e3e4;
    --white: #ffffff;
  }
  * { margin: 0; padding: 0; box-sizing: border-box; }
  html, body { width: 849px; height: 1200px; overflow: hidden; background: var(--white); }
  .flyer {
    position: relative; width: 849px; height: 1200px; overflow: hidden;
    font-family: "Arimo", Arial, sans-serif; color: var(--text); font-size: 13px;
  }
  .header-wave { position: absolute; left: 0; top: 0; width: 849px; height: 210px; }
  .title {
    position: absolute; top: 48px; left: 0; width: 849px; text-align: center;
    color: var(--white); font-weight: 700; font-size: 30px; letter-spacing: 0.3px;
  }
  .subtitle {
    position: absolute; top: 88px; left: 0; width: 849px; text-align: center;
    color: var(--white); font-weight: 700; font-style: italic; font-size: 13.5px; letter-spacing: 1.7px;
  }
  .brand {
    position: absolute; left: 176px; top: 254px;
    color: var(--ink-navy); font-size: 29px; line-height: 29px; letter-spacing: 1.5px; font-weight: 400;
  }
  .brand-mark {
    position: absolute; left: 44px; top: 262px; width: 110px; height: 72px; background: var(--gold);
  }
  .hero-photo {
    position: absolute; left: 505px; top: 195px; width: 360px; height: 331px;
    border-radius: 16px; border: 1px solid #333;
    background: linear-gradient(135deg, #dfe6ec 0%, #a8b0b8 45%, #5d6268 100%);
  }
  .heading {
    font-family: "Roboto Condensed", "Arial Narrow", sans-serif; font-weight: 700; color: var(--ink-navy);
  }
  .intro { position: absolute; left: 42px; top: 376px; }
  .intro .heading { font-size: 18px; line-height: 26px; }
  .bullets { list-style: none; font-size: 13px; }
  .bullets li { line-height: 25.7px; }
  .bullets li::before { content: "• "; }
  .indent { padding-left: 11px; }
  .audience { position: absolute; left: 42px; top: 494px; }
  .audience .heading { font-size: 16px; line-height: 26px; margin-bottom: 6px; }
  .details { position: absolute; left: 42px; top: 586px; width: 460px; }
  .details p { line-height: 34.6px; white-space: nowrap; }
  .details .label { font-size: 18px; }
  .details .note { line-height: 18px; margin-top: 0; }
  .register {
    position: absolute; left: 32px; top: 756px; width: 321px; height: 32px;
    background: var(--box-grey); border: 1px solid #a9a9ab;
    color: var(--ink-navy); font-family: "Roboto Condensed", "Arial Narrow", sans-serif; font-weight: 700;
    font-size: 19px; line-height: 30px; padding-left: 10px; letter-spacing: 0.4px;
  }
  .programme { position: absolute; left: 42px; top: 806px; width: 450px; line-height: 25.7px; }
  .programme .label { font-size: 19px; }
  .schedule-title { position: absolute; left: 33px; top: 930px; font-size: 18px; }
  .schedule {
    position: absolute; left: 31px; top: 962px; width: 466px;
    border: 1px solid var(--rule); border-radius: 14px; overflow: hidden;
    border-collapse: separate; border-spacing: 0; font-size: 11.5px;
  }
  .schedule th {
    background: var(--ink-navy); color: var(--white); font-weight: 700; height: 27px; font-size: 12px; letter-spacing: 0.4px;
  }
  .schedule td { border-top: 1px solid var(--rule); padding: 0 10px; vertical-align: middle; line-height: 22px; }
  .schedule td + td, .schedule th + th { border-left: 1px solid var(--rule); }
  .schedule .session { padding-left: 11px; }
  .schedule .tall { height: 51px; }
  .schedule .short { height: 25px; }
  .schedule .mid { height: 29px; }
  .theme { position: absolute; left: 557px; top: 560px; width: 262px; line-height: 25.65px; }
  .theme .label { font-size: 18px; }
  .footer-band {
    position: absolute; left: 0; top: 1153px; width: 849px; height: 47px; background: var(--gold);
    color: var(--white); font-family: "Roboto Condensed", "Arial Narrow", sans-serif; font-weight: 700;
    font-size: 16.5px; line-height: 47px; text-align: center; white-space: nowrap;
  }
</style>
</head>
<body>
<div class="flyer">
  <svg class="header-wave" viewBox="0 0 849 210" aria-hidden="true">
    <path d="M0 0 H849 V210 C800 165 720 140 600 132 C430 122 300 160 150 168 C80 170 30 160 0 148 Z" fill="var(--gold)"/>
    <path d="M0 0 H849 V190 C800 150 720 128 600 125 C430 120 300 150 150 152 C80 152 30 138 0 124 Z" fill="var(--navy)"/>
  </svg>
  <h1 class="title">TRV Educational Workshop</h1>
  <p class="subtitle">“The Essentials of Strata Living – What Every Owner Needs to Know” 12th and 26th June 2010</p>

  <div class="brand-mark" aria-hidden="true"></div>
  <div class="brand">TOWER<br>RESIDENTS<br>VOICE</div>

  <div class="hero-photo" role="img" aria-label="Photo of three smiling business people in suits standing in a bright office"></div>

  <section class="intro">
    <h2 class="heading">This Workshop Is For Owners In Strata Apartments<br>Who Want To Learn More About:</h2>
    <ul class="bullets">
      <li>Getting the best out of apartment living</li>
      <li>Protecting their home and their investment</li>
    </ul>
  </section>

  <section class="audience">
    <h2 class="heading">AND particularly for...</h2>
    <ul class="bullets">
      <li>Executive committee members to know their rights</li>
      <li class="indent" style="list-style:none">and responsibilities in managing their strata scheme</li>
    </ul>
  </section>
  <style>.audience .indent::before{content:"";}</style>

  <section class="details">
    <p><span class="heading label">Location:</span> Harbourside Club 24 Bayview Terrace Northpoint 2061</p>
    <p><span class="heading label">Dates:</span> The workshop will run twice – on 12th June and 26th June 2010</p>
    <p><span class="heading label">Time:</span> 10.00 am to 4.00 pm.</p>
    <p><span class="heading label">Cost:</span> $60.00, which includes morning tea and lunch.</p>
    <p class="note">The maximum number of participants for each workshop is 60.</p>
  </section>

  <div class="register">Register Online at: www.trv.org.au</div>

  <p class="programme"><span class="heading label">Programme:</span> The day will comprise four sessions, each facilitated by a specialist. In each session the speaker will provide relevant information and set the topics for group work; participants will break into groups and work up solutions to each topic; and the groups will compare outcomes.</p>

  <h2 class="heading schedule-title">Conference Schedule:</h2>
  <table class="schedule">
    <colgroup><col style="width:80px"><col style="width:115px"><col></colgroup>
    <thead><tr><th></th><th>Topic</th><th>Speaker</th></tr></thead>
    <tbody>
      <tr class="short"><td class="session" rowspan="2">Morning</td><td>Governance</td><td>Martin Lowe, strata lawyer</td></tr>
      <tr class="tall"><td style="vertical-align:top;padding-top:2px">Management</td><td>Stephen Aldous, seasoned former chairperson and executive committee member</td></tr>
      <tr class="short"><td class="session" rowspan="2">Afternoon</td><td>Financials</td><td>Peter Whitcombe, accountant</td></tr>
      <tr class="mid"><td>Physicality</td><td>David Rennick, facilities manager</td></tr>
    </tbody>
  </table>

  <p class="theme"><span class="heading label">The Day’s Theme Will Be:</span> Gina is a new owner in her building called Utopia Tower. She notices some management processes which to her seem strange. She is elected to the executive committee and finds that the developer has retained more control than she realised - the service providers have long-term and onerous contracts, and she doesn’t seem to be able to exert enough influence. What does the law require her to do, as a committee member? How does she influence good management processes? The finances seem to be out of control, so how can she fix them so she doesn’t pay inflated levies each year and lose value on her investment? ... and then the neighbour above her apartment installs a timber floor and she has noise problems ... and the building seems to have a lot of defects.</p>

  <div class="footer-band">Enroll Now - Learn A Lot - Have Some Fun As Well - Share Experiences - Find Out How TRV Can Help You In The Longer Term</div>
</div>
</body>
</html>
```